We need an attractive business card design that is modern and inviting. We like the blue and yellow (or gold) colors that are displayed with the logo. The business should communicate trust, experience, and integrity.

Target Market(s)

Residential and Commercial

Industry/Entity Type

Business

Contact Information for Business Card

Recessed Lighting
LED Retro Fit
Sign Repair
Alarms and Cameras
Mobile Home Services
24hr service calls

Font styles to use
Serif
Sans Serif

Colors
3176b5
0455a3
fece3e
fbee3e

Requirements
Must have
• Brannick Electric
• Owner: Marcus Brannick
• Licensed and Insured
• TECL #58731
Nice to have
• Exquisite Detail!!
• Over 20 years of experience
Should not have
• Nothing boring or traditional!!!

```html
<!DOCTYPE html>
<html lang="en">
<head>
<meta charset="utf-8">
<title>Brannick Electric – Business Cards</title>
<link rel="stylesheet" href="https://fonts.googleapis.com/css2?family=Arimo:wght@400;700&family=Archivo+Narrow:wght@400;500&display=swap">
<style>
  :root {
    --stage: #2f2b29;
    --card: #141517;
    --blue: #1f5fb0;
    --blue-deep: #0455a3;
    --yellow: #fece3e;
    --text: #e6e6e6;
    --muted: #a9abae;
    --rule: #8d8f93;
  }
  * { margin: 0; padding: 0; box-sizing: border-box; }
  html, body { width: 1200px; height: 864px; overflow: hidden; }
  body {
    background: var(--stage);
    font-family: "Arimo", Arial, sans-serif;
    position: relative;
  }
  .card {
    position: absolute;
    top: 277px;
    width: 540px;
    height: 309px;
    background: var(--card);
    border-radius: 4px;
    box-shadow: 0 10px 30px rgba(0,0,0,.45);
    overflow: hidden;
  }
  .card--front { left: 40px; }
  .card--back { left: 620px; }

  .brand-mark {
    position: absolute;
    width: 56px;
    height: 56px;
    border: 4px solid var(--blue);
    border-radius: 50%;
  }
  .brand-name {
    position: absolute;
    left: 0; right: 0;
    text-align: center;
    font-weight: 700;
    color: var(--yellow);
    letter-spacing: 1px;
    text-transform: uppercase;
  }

  /* front */
  .card--front .brand-mark { left: 242px; top: 34px; }
  .card--front .brand-name { top: 104px; font-size: 34px; }
  .tagline {
    position: absolute;
    left: 0; right: 0; top: 150px;
    text-align: center;
    color: var(--blue);
    font-size: 21px;
  }
  .services {
    position: absolute;
    left: 0; right: 0; top: 196px;
    list-style: none;
    text-align: center;
    font-family: "Archivo Narrow", "Arial Narrow", sans-serif;
    font-size: 16px;
    line-height: 24px;
    color: var(--muted);
  }
  .services .dot { color: var(--blue); margin: 0 6px; }

  /* back */
  .card--back .brand-mark { left: 348px; top: 26px; }
  .card--back .brand-name { top: 92px; font-size: 30px; padding-left: 60px; }
  .holder {
    position: absolute;
    right: 282px; top: 140px;
    text-align: right;
  }
  .holder-name { color: var(--blue); font-size: 20px; }
  .holder-role { color: var(--yellow); font-size: 15px; margin-top: 3px; }
  .address {
    position: absolute;
    right: 282px; top: 196px;
    text-align: right;
    color: var(--text);
    font-size: 14px;
    line-height: 22px;
  }
  .divider {
    position: absolute;
    left: 270px; top: 150px;
    width: 1px; height: 130px;
    background: linear-gradient(var(--card), var(--rule) 30%, var(--rule) 70%, var(--card));
  }
  .contacts {
    position: absolute;
    left: 290px; top: 160px;
    list-style: none;
    color: var(--text);
    font-size: 15px;
    line-height: 25px;
  }
  .contacts li { display: flex; align-items: center; gap: 10px; }
  .contacts svg { width: 16px; height: 16px; fill: var(--blue); flex: none; }
  .credentials {
    position: absolute;
    left: 290px; top: 240px;
    color: var(--text);
    font-size: 15px;
    line-height: 21px;
  }
</style>
</head>
<body>

<section class="card card--front">
  <span class="brand-mark"></span>
  <h1 class="brand-name">Brannick Electric</h1>
  <p class="tagline">Over 20 years of experience</p>
  <ul class="services">
    <li>Residential and Commercial<span class="dot">●</span>Recessed Lighting</li>
    <li>LED Retro Fit<span class="dot">●</span>Sign Repair<span class="dot">●</span>Alarms and Cameras</li>
    <li>Mobile Home Services<span class="dot">●</span>24hr service calls</li>
  </ul>
</section>

<section class="card card--back">
  <span class="brand-mark"></span>
  <h2 class="brand-name">Brannick Electric</h2>

  <div class="holder">
    <p class="holder-name">Marcus Brannick</p>
    <p class="holder-role">Owner</p>
  </div>
  <address class="address" style="font-style:normal">
    4127 Harrow Lane<br>
    Maple Ridge, NY 11920<br>
    www.brannickelec.com
  </address>

  <span class="divider"></span>

  <ul class="contacts">
    <li>
      <svg viewBox="0 0 16 16" aria-hidden="true"><path d="M2 5c0-2 2-3 6-3s6 1 6 3v1h-3V5H5v1H2zM4 7h8l2 6H2zm4 1.5a2 2 0 1 0 0 4 2 2 0 0 0 0-4z"/></svg>
      555 0142 2210
    </li>
    <li>
      <svg viewBox="0 0 16 16" aria-hidden="true"><path d="M4.5 1h7a1 1 0 0 1 1 1v12a1 1 0 0 1-1 1h-7a1 1 0 0 1-1-1V2a1 1 0 0 1 1-1zm.7 2v9h5.6V3zM8 12.6a.8.8 0 1 0 0 1.6.8.8 0 0 0 0-1.6z"/></svg>
      555 0187 4396
    </li>
    <li>
      <svg viewBox="0 0 16 16" aria-hidden="true"><path d="M1 4h14v1L8 9.5 1 5zm0 2.4 7 4.4 7-4.4V13H1z"/></svg>
      marcus@brannickelec.com
    </li>
  </ul>
  <p class="credentials">Licensed and Insured<br>TECL #58731</p>
</section>

</body>
</html>
```